PowerPoint Template Design for Management Consultancy

I need a PPT template for a new management consulting company. I want a modern look that uses dark blues and greys for divider slides, white content slides and a creative use of the logo in the slides. The supplied images are used on the website so I'd like to incorporate these into the theme

Target Market(s)

Management Consulting

Industry/Entity Type

Consulting

Font styles to use
Sans Serif

Colors
3277b5

Requirements
Must have
• Options for title slide, divider slides, content slides using the logo provided
Plain white content slides with creative use of logo
Color theme uses dark blues and greys
Nice to have
• Light and dark theme

```html
<!DOCTYPE html>
<html lang="en">
<head>
<meta charset="utf-8">
<title>Arvelo Consulting – Presentation Template</title>
<link rel="stylesheet" href="https://fonts.googleapis.com/css2?family=Quicksand:wght@500;700&family=Arimo:wght@400&display=swap">
<style>
  :root {
    --page: #f3f3f3;
    --navy: #1b3461;
    --navy-deep: #142a52;
    --blue: #2a4f8f;
    --grey: #5c5c5c;
    --grey-light: #8a8a8a;
    --text: #555;
    --white: #fff;
    --card-line: #e6e6e6;
  }
  * { box-sizing: border-box; margin: 0; padding: 0; }
  html, body { width: 1200px; height: 4208px; overflow: hidden; background: var(--page); }
  body { position: relative; font-family: "Arimo", Arial, sans-serif; color: var(--text); }
  .slide {
    position: absolute; left: 51px; width: 1097px; height: 619px;
    background: var(--white); overflow: hidden;
    box-shadow: 0 1px 4px rgba(0,0,0,.12);
  }
  .slide--content {
    border-top: 4px solid var(--navy);
    background: radial-gradient(ellipse at 30% 70%, #f3f4f6 0%, #fff 60%);
  }
  .header-band {
    position: absolute; left: 0; top: 0; width: 355px; height: 50px;
    background: var(--navy);
    clip-path: polygon(0 0, 100% 0, 95% 100%, 0 100%);
    color: var(--white); font-family: "Quicksand", sans-serif; font-weight: 700;
    font-size: 22px; letter-spacing: .5px; line-height: 50px; padding-left: 34px;
  }
  .brand-small {
    position: absolute; right: 36px; top: 14px;
    font-family: "Quicksand", sans-serif; font-weight: 700; font-size: 22px;
    color: var(--navy); letter-spacing: 1px;
  }
  .display { font-family: "Quicksand", sans-serif; font-weight: 700; }
  .photo { position: absolute; }
  .body-copy { font-size: 11.5px; line-height: 21.5px; color: var(--text); }
  .body-copy p + p { margin-top: 21px; }

  /* title slide */
  .title-photo { inset: 0; background: linear-gradient(180deg, #f2ece4 0%, #d8dde4 35%, #8fa6c0 60%, #5d7898 85%, #3a4f6a 100%); }
  .title-brand { position: absolute; left: 90px; top: 78px; width: 420px; text-align: center; color: var(--navy); line-height: 1; }
  .title-brand__name { display: block; font-size: 80px; letter-spacing: 3px; }
  .title-brand__sub { display: block; margin-top: 8px; font-size: 28px; letter-spacing: 3px; }

  /* intro */
  .intro-brand { position: absolute; left: 60px; top: 260px; font-size: 66px; color: var(--navy); letter-spacing: 2px; }
  .intro-divider { position: absolute; left: 472px; top: 140px; width: 1px; height: 365px; background: #cfcfcf; }
  .intro-text { position: absolute; left: 521px; top: 138px; width: 527px; }

  /* numbered list */
  .point { position: absolute; width: 470px; height: 90px; }
  .point__num {
    position: absolute; left: 0; top: 0; width: 85px; height: 85px; border-radius: 50%;
    color: var(--white); font-size: 30px; line-height: 85px; text-align: center;
  }
  .point__num--navy { background: var(--navy); }
  .point__num--grey { background: var(--grey); }
  .point__title { position: absolute; left: 111px; top: 5px; font-size: 14px; color: var(--navy); }
  .point__text { position: absolute; left: 111px; top: 27px; width: 378px; font-size: 10px; line-height: 17px; color: var(--text); }

  /* feature */
  .feature-title { position: absolute; left: 47px; top: 130px; width: 470px; font-size: 21px; line-height: 32px; color: var(--blue); }
  .feature-text { position: absolute; left: 47px; top: 210px; width: 461px; text-align: justify; }
  .feature-photo { left: 575px; top: 103px; width: 477px; height: 462px; background: linear-gradient(180deg, #1f3f8e 0%, #3d66a8 40%, #d7a760 68%, #4b4d55 82%, #1e1f24 100%); }

  /* team */
  .card { position: absolute; top: 139px; width: 253px; height: 421px; background: var(--white); box-shadow: 0 0 3px rgba(0,0,0,.12); text-align: center; }
  .card__photo { position: relative; width: 100%; height: 216px; background: linear-gradient(180deg, #bdb8b2 0%, #8e8780 100%); }
  .card__name { margin-top: 38px; font-size: 15px; color: var(--navy); letter-spacing: .5px; }
  .card__role { margin-top: 4px; font-size: 11px; color: var(--text); }
  .card__text { margin: 18px auto 0; width: 222px; font-size: 9.5px; line-height: 19px; color: var(--text); }

  /* closing */
  .slide--dark { background: var(--navy); }
  .closing-photo { inset: 0; background: linear-gradient(180deg, #1e3a6b 0%, #1b3461 55%, #1f3a66 75%, #172d55 100%); }
  .closing-mark { position: absolute; left: 50%; top: 150px; transform: translateX(-50%); display: flex; align-items: center; gap: 18px; }
  .closing-mark__square { width: 34px; height: 34px; background: var(--white); }
  .closing-mark__name { font-size: 60px; color: var(--white); letter-spacing: 3px; }
  .closing-title { position: absolute; left: 0; right: 0; top: 348px; text-align: center; font-size: 90px; color: var(--white); letter-spacing: 4px; }
</style>
</head>
<body>

<!-- Title slide -->
<section class="slide" style="top:82px">
  <div class="photo title-photo" role="img" aria-label="Misty blue mountain ranges with two climbers helping each other on a dark cliff at right"></div>
  <div class="title-brand display">
    <span class="title-brand__name">ARVELO</span>
    <span class="title-brand__sub">CONSULTING</span>
  </div>
</section>

<!-- Introduction -->
<section class="slide slide--content" style="top:762px">
  <div class="header-band">INTRODUCTION</div>
  <div class="brand-small">ARVELO</div>
  <div class="intro-brand display">ARVELO</div>
  <div class="intro-divider"></div>
  <div class="intro-text body-copy">
    <p>Sed ut perspiciatis unde omnis iste natus error sit voluptatem accusantium doloremque laudantium, totam rem aperiam, eaque ipsa quae ab illo inventore veritatis et quasi architecto beatae vitae dicta sunt explicabo. Nemo enim ipsam voluptatem quia voluptas sit aspernatur aut odit aut fugit, sed quia consequuntur magni dolores eos qui ratione voluptatem sequi nesciunt. Neque porro quisquam est, qui dolorem ipsum quia dolor sit amet, consectetur, adipisci velit, sed quia non numquam eius modi tempora incidunt ut labore et dolore magnam aliquam quaerat voluptatem.</p>
    <p>Sed ut perspiciatis unde omnis iste natus error sit voluptatem accusantium doloremque laudantium, totam rem aperiam, eaque ipsa quae ab illo inventore veritatis et quasi architecto beatae vitae dicta sunt explicabo. Nemo enim ipsam voluptatem quia voluptas sit aspernatur aut odit aut fugit, sed quia consequuntur magni dolores eos qui ratione voluptatem sequi nesciunt. Neque porro quisquam est, qui dolorem ipsum quia dolor sit amet, consectetur, adipisci velit, sed quia non numquam eius modi tempora incidunt ut labore et dolore magnam aliquam quaerat voluptatem.</p>
    <p>Ut enim ad minima veniam, quis nostrum exercitationem ullam corporis suscipit laboriosam, nisi ut ali quid ex ea commodi consequatur uis autem vel eum iure reprehenderit qui in ea voluptate velit esse vel illum qui dolorem eum fugiat quo voluptas nulla pariatur</p>
  </div>
</section>

<!-- Numbered points -->
<section class="slide slide--content" style="top:1450px">
  <div class="header-band">YOUR TITLE HERE</div>
  <div class="brand-small">ARVELO</div>

  <div class="point" style="left:18px;top:142px">
    <div class="point__num point__num--navy display">01</div>
    <div class="point__title display">SED UT PERSPICIATIS UNDE</div>
    <div class="point__text">Nemo enim ipsam voluptatem quia voluptas sit aspernatur aut odit aut fugit, sedqui a consequuntur magni dolores eos qui ratione voluptatem sequi nesciunt. Neque dolorem ipsum quia dolor sit amet, consectetur, adipisci velit,</div>
  </div>
  <div class="point" style="left:18px;top:291px">
    <div class="point__num point__num--grey display">02</div>
    <div class="point__title display">SED UT PERSPICIATIS UNDE</div>
    <div class="point__text">Nemo enim ipsam voluptatem quia voluptas sit aspernatur aut odit aut fugit, sedqui a consequuntur magni dolores eos qui ratione voluptatem sequi nesciunt. Neque dolorem ipsum quia dolor sit amet, consectetur, adipisci velit,</div>
  </div>
  <div class="point" style="left:18px;top:440px">
    <div class="point__num point__num--navy display">03</div>
    <div class="point__title display">SED UT PERSPICIATIS UNDE</div>
    <div class="point__text">Nemo enim ipsam voluptatem quia voluptas sit aspernatur aut odit aut fugit, sedqui a consequuntur magni dolores eos qui ratione voluptatem sequi nesciunt. Neque dolorem ipsum quia dolor sit amet, consectetur, adipisci velit,</div>
  </div>
  <div class="point" style="left:591px;top:142px">
    <div class="point__num point__num--grey display">04</div>
    <div class="point__title display">SED UT PERSPICIATIS UNDE</div>
    <div class="point__text">Nemo enim ipsam voluptatem quia voluptas sit aspernatur aut odit aut fugit, sedqui a consequuntur magni dolores eos qui ratione voluptatem sequi nesciunt. Neque dolorem ipsum quia dolor sit amet, consectetur, adipisci velit,</div>
  </div>
  <div class="point" style="left:591px;top:291px">
    <div class="point__num point__num--navy display">05</div>
    <div class="point__title display">SED UT PERSPICIATIS UNDE</div>
    <div class="point__text">Nemo enim ipsam voluptatem quia voluptas sit aspernatur aut odit aut fugit, sedqui a consequuntur magni dolores eos qui ratione voluptatem sequi nesciunt. Neque dolorem ipsum quia dolor sit amet, consectetur, adipisci velit,</div>
  </div>
  <div class="point" style="left:591px;top:440px">
    <div class="point__num point__num--grey display">06</div>
    <div class="point__title display">SED UT PERSPICIATIS UNDE</div>
    <div class="point__text">Nemo enim ipsam voluptatem quia voluptas sit aspernatur aut odit aut fugit, sedqui a consequuntur magni dolores eos qui ratione voluptatem sequi nesciunt. Neque dolorem ipsum quia dolor sit amet, consectetur, adipisci velit,</div>
  </div>
</section>

<!-- Feature with image -->
<section class="slide slide--content" style="top:2158px">
  <div class="header-band">YOUR TITLE HERE</div>
  <div class="brand-small">ARVELO</div>
  <h2 class="feature-title display">SED UT PERSPICIATIS UNDE OMNIS ISTE NATUS ERROR SIT</h2>
  <div class="feature-text body-copy">
    <p>Sed ut perspiciatis unde omnis iste natus error sit voluptatem accusantium doloremque laudantium, totam rem aperiam, eaque ipsa quae ab illo inventore veritatis et quasi arc hitecto beatae vitae dicta sunt explicabo. Nemo enim ipsam voluptatem quia voluptas sit aspernatur aut odit aut fugit, sed quia consequuntur magni dolores eos qui ratione volu ptatem sequi nesciunt. Neque porro quisquam est, qui dolorem ipsum quia dolor sit amet, consectetur, adipisci velit, sed quia non numquam eius modi tempora incidunt ut labore et dolore magnam aliquam quaerat voluptatem.</p>
    <p>Sed ut perspiciatis unde omnis iste natus error sit voluptatem accusantium doloremque laudantium, totam rem aperiam, eaque ipsa quae ab illo inventore veritatis et quasi arch itecto beatae vitae dicta sunt explicabo. Nemo enim ipsam voluptatem quia voluptas sit aspernatur aut odit aut fugit, sed quia consequuntur magni dolores eos qui ratione volu ptatem sequi nesciunt. Neque porro quisquam est, qui dolorem ipsum quia dolor sit amet, consectetur, adipisci velit, sed quia non numquam eius modi tempora incidunt ut labore et dolore magnam aliquam quaerat voluptatem.</p>
  </div>
  <div class="photo feature-photo" role="img" aria-label="Two hikers raising their arms on a mountain top at sunset under a deep blue sky"></div>
</section>

<!-- Team -->
<section class="slide slide--content" style="top:2851px">
  <div class="header-band">YOUR TITLE HERE</div>
  <div class="brand-small">ARVELO</div>

  <article class="card" style="left:20px">
    <div class="card__photo" role="img" aria-label="Portrait photo of a team member"></div>
    <div class="card__name display">DANA WHITCOMBE</div>
    <div class="card__role">Consulting</div>
    <p class="card__text">Sed ut perspiciatis unde omnis iste natus error sit voluptatem accusantium dolore mque laudant ium, totam rem aperiam, eaque ipsa quae ab illo inventore veritatis et quasi architecto beatae vitae dicta sunt explicabo.</p>
  </article>
  <article class="card" style="left:288px">
    <div class="card__photo" role="img" aria-label="Portrait photo of a team member"></div>
    <div class="card__name display">DANA WHITCOMBE</div>
    <div class="card__role">Consulting</div>
    <p class="card__text">Sed ut perspiciatis unde omnis iste natus error sit voluptatem accusantium dolore mque laudant ium, totam rem aperiam, eaque ipsa quae ab illo inventore veritatis et quasi architecto beatae vitae dicta sunt explicabo.</p>
  </article>
  <article class="card" style="left:556px">
    <div class="card__photo" role="img" aria-label="Portrait photo of a team member"></div>
    <div class="card__name display">DANA WHITCOMBE</div>
    <div class="card__role">Consulting</div>
    <p class="card__text">Sed ut perspiciatis unde omnis iste natus error sit voluptatem accusantium dolore mque laudant ium, totam rem aperiam, eaque ipsa quae ab illo inventore veritatis et quasi architecto beatae vitae dicta sunt explicabo.</p>
  </article>
  <article class="card" style="left:824px">
    <div class="card__photo" role="img" aria-label="Portrait photo of a team member"></div>
    <div class="card__name display">DANA WHITCOMBE</div>
    <div class="card__role">Consulting</div>
    <p class="card__text">Sed ut perspiciatis unde omnis iste natus error sit voluptatem accusantium dolore mque laudant ium, totam rem aperiam, eaque ipsa quae ab illo inventore veritatis et quasi architecto beatae vitae dicta sunt explicabo.</p>
  </article>
</section>

<!-- Closing -->
<section class="slide slide--dark" style="top:3532px">
  <div class="photo closing-photo" role="img" aria-label="Faint navy-toned mountain silhouette with two hikers raising their arms"></div>
  <div class="closing-mark">
    <span class="closing-mark__square"></span>
    <span class="closing-mark__name display">ARVELO</span>
  </div>
  <div class="closing-title display">THANK YOU</div>
</section>

</body>
</html>
```